Updated flyer

We've decided to do this as a house party, the info is below. For this you can use a model or not use one, either way is fine. I attached two logos and some designs we've used from pixel harbor before. I also attached a pic with a duck that you can use as the background
TIDE SWAY
(Pool Party Edition)
July 13 2013
Featuring DJs
Vantor (logo) Kemble (logo)
Lionel Hartwick Marty Oakes
brindlepage.com/vantor87 for address (Natomas, invite only)
Full Bar/Food/Water Basketball/Pool Table/Fun
Reason: I changed the info since it's a house party now so I didn't want to rush to close. It is a guaranteed project though thx
21-40 year old house music lounge lovers
House

```html
<!DOCTYPE html>
<html lang="en">
<head>
<meta charset="utf-8">
<title>Tide Sway – Pool Party Edition</title>
<link rel="stylesheet" href="https://fonts.googleapis.com/css2?family=Bubblegum+Sans&family=Cinzel:wght@700&family=Fredoka:wght@600;700&display=swap">
<style>
  :root {
    --page-bg: #e6e7e8;
    --sky-light: #e4f3fd;
    --sky-mid: #8cc8ef;
    --sky-deep: #3f8fd0;
    --navy: #1b3346;
    --navy-soft: #2f5a76;
    --ink: #151b22;
    --white: #ffffff;
    --ice: #a9dcf6;
    --ice-deep: #5fb3e4;
  }
  * { margin: 0; padding: 0; box-sizing: border-box; }
  html, body { width: 1200px; height: 900px; overflow: hidden; background: var(--page-bg); }
  .flyer {
    position: absolute; left: 315px; top: 46px;
    width: 570px; height: 808px; overflow: hidden;
    background: var(--navy);
  }
  .flyer__art {
    position: absolute; left: 0; top: 0; width: 570px; height: 600px;
    background:
      linear-gradient(to bottom, rgba(27,51,70,0) 78%, var(--navy) 100%),
      radial-gradient(circle at 42% 52%, var(--sky-light) 0%, var(--sky-mid) 40%, var(--sky-deep) 100%);
  }
  .flyer__figure {
    position: absolute; left: 330px; top: 110px; width: 200px; height: 520px;
    border-radius: 100px 100px 20px 20px;
    background: linear-gradient(to bottom, rgba(214,160,72,0.55), rgba(63,143,208,0.5));
  }
  .flyer__band {
    position: absolute; left: 0; top: 590px; width: 570px; height: 218px;
    background: linear-gradient(to bottom, var(--navy) 0%, var(--navy-soft) 100%);
  }
  .date {
    position: absolute; left: 22px; top: 134px;
    font: 48px "Bubblegum Sans", cursive; color: var(--white);
    -webkit-text-stroke: 2px var(--ink); paint-order: stroke fill;
    text-shadow: 3px 3px 0 var(--ink);
  }
  .featuring {
    position: absolute; left: 166px; top: 224px;
    font: 700 17px "Cinzel", serif; color: var(--ink); letter-spacing: 0.5px;
  }
  .dj-marks {
    position: absolute; left: 22px; top: 256px;
    display: flex; align-items: center; gap: 26px;
  }
  .dj-mark { font: 700 36px "Fredoka", sans-serif; color: var(--ink); letter-spacing: 1px; }
  .lineup {
    position: absolute; left: 22px; top: 344px; list-style: none;
    font: 700 32px/42px "Fredoka", sans-serif; color: var(--ink);
  }
  .web {
    position: absolute; left: 30px; top: 440px;
    font: 700 13px "Cinzel", serif; color: var(--ink); letter-spacing: 0.3px;
  }
  .address-note {
    position: absolute; left: 30px; top: 460px;
    font: 700 12px "Cinzel", serif; color: var(--ink); letter-spacing: 0.3px;
  }
  .title {
    position: absolute; left: 0; top: 606px; width: 570px; text-align: center;
    font: 84px "Bubblegum Sans", cursive; color: var(--ice); letter-spacing: 2px;
    -webkit-text-stroke: 4px var(--white); paint-order: stroke fill;
    text-shadow: 0 3px 0 var(--ice-deep);
  }
  .subtitle {
    position: absolute; left: 0; top: 708px; width: 570px; text-align: center;
    font: 700 28px "Fredoka", sans-serif; color: var(--white);
  }
  .amenities {
    position: absolute; left: 0; top: 768px; width: 570px; text-align: center;
    font: 700 15px "Cinzel", serif; color: var(--white); letter-spacing: 0.4px;
  }
</style>
</head>
<body>
<main class="flyer">
  <div class="flyer__art" role="img" aria-label="Blue sunburst background with palm fronds, pink tropical flowers and a cheering crowd silhouette"></div>
  <div class="flyer__figure" role="img" aria-label="Illustrated woman in a blue swimsuit holding a cocktail"></div>
  <div class="flyer__band"></div>

  <p class="date">July 13 2013</p>
  <p class="featuring">FEATURING DJS</p>
  <div class="dj-marks">
    <span class="dj-mark">Vantor</span>
    <span class="dj-mark">Kemble</span>
  </div>
  <ul class="lineup">
    <li>Lionel Hartwick</li>
    <li>Marty Oakes</li>
  </ul>
  <p class="web">BRINDLEPAGE.COM/VANTOR87</p>
  <p class="address-note">FOR ADDRESS (NATOMAS, INVITE ONLY)</p>

  <h1 class="title">TIDE SWAY</h1>
  <p class="subtitle">(Pool Party Edition)</p>
  <p class="amenities">FULL BAR / FOOD / WATER BASKETBALL / POOL TABLE / FUN</p>
</main>
</body>
</html>
```